Tobias Wrenfield - Cinematographer

NEED:
I'm looking for a sleek, professional, modern business card that will give give the recipient the impression that they can trust their production will go smoothly by hiring me. I will bring creativity and knowledge to their shoot, so that we can create powerful images.
I am looking for a card with a strong style and design ethos that could be expanded to a website and a full visual/graphic/design entity for me.
ABOUT ME:
I am a mid-twenties cinematographer, I work on music video, narrative short, commercial, and corporate projects. I blend the science and artistry of cameras and filmmaking to tell a story. I'm an artist, a technician, and a manager.
DESIGN:
I like sleek, simple design. Black, dark grays, white, dark navy, steel blues, I love cyan, but also cyan and red. I am not a fan of earthy tones. I generally prefer modern, san-serif fonts over serifs. My old logo was based on an aperture, a multi-blade device at the back of a lens that controls how much light passes through, but I made it with so many colors, that it doesn't necessarily lend itself to a specific color-scheme or design ethos. I liked that the aperture design provided a sense of the technical requirements of my job. I'm a fan of matte business cards, but am open to plenty of specialty print processes to make an outstanding card.
ATTACHED FILES:
My Old Rainbox Aperture Logo, plus a few designs I've tried playing around with, but am not tied to. I AM OPEN TO NEW DESIGNS, DO NOT FEEL TIED TO THIS.
**I've pulled my old logo down from the attached files, and instead attached other business cards I like, so as not to mislead you where I would like to go.
INFO:
Name: Tobias Wrenfield
Job: Cinematographer
Email: tkwrenfield@quillbox.example
Phone: 503.618.2907
Website: tobiaswrenfield.example
Updates
I'm adding some images of other cards that I like, and removing my old logo, since I'm looking for something new, and don't want that old logo to push anyone a certain direction.

```html
<!DOCTYPE html>
<html lang="en">
<head>
<meta charset="utf-8">
<title>Tobias Wrenfield – Cinematographer Business Card</title>
<link rel="stylesheet" href="https://fonts.googleapis.com/css2?family=Montserrat:wght@400;500;700&display=swap">
<style>
  :root {
    --page-bg: #e9e9ec;
    --card-black: #141416;
    --card-charcoal: #2a2a2e;
    --card-white: #f7f7f8;
    --card-grey: #e4e4e6;
    --accent-cyan: #1aa3e0;
    --text-light: #ffffff;
    --text-muted: #c9c9cc;
    --text-dark: #2b2b2e;
    --icon-blue: #1a6fd0;
  }
  * { box-sizing: border-box; margin: 0; padding: 0; }
  html, body {
    width: 1200px; height: 913px; overflow: hidden;
    background: var(--page-bg);
    font-family: "Montserrat", Arial, sans-serif;
  }
  .sheet {
    position: relative; width: 1200px; height: 913px;
    display: flex; align-items: center; justify-content: center; gap: 50px;
  }
  .card {
    position: relative; width: 530px; height: 303px;
    border-radius: 4px; overflow: hidden;
    box-shadow: 0 10px 28px rgba(0,0,0,0.22);
  }
  /* Front */
  .card--front {
    background: linear-gradient(150deg, var(--card-charcoal) 0%, var(--card-black) 70%);
  }
  .wordmark {
    position: absolute; left: 0; right: 0; top: 50%;
    transform: translateY(-50%);
    display: flex; flex-direction: column; align-items: center; gap: 8px;
  }
  .wordmark__row { display: flex; align-items: center; gap: 14px; }
  .wordmark__dot {
    width: 26px; height: 26px; border-radius: 50%;
    background: var(--accent-cyan);
  }
  .wordmark__name {
    color: var(--text-light); font-weight: 500;
    font-size: 30px; letter-spacing: 2px; text-transform: uppercase;
  }
  .wordmark__role {
    color: var(--text-muted); font-weight: 400;
    font-size: 15px; letter-spacing: 6px; text-transform: uppercase;
  }
  /* Back */
  .card--back { background: var(--card-white); }
  .card__shape { position: absolute; inset: 0; width: 100%; height: 100%; }
  .card--back .wordmark { top: 26%; }
  .card--back .wordmark__name { font-size: 19px; letter-spacing: 1.5px; }
  .card--back .wordmark__dot { width: 16px; height: 16px; }
  .card--back .wordmark__role { font-size: 10px; letter-spacing: 4px; }
  .card--back .wordmark { gap: 5px; }
  .identity {
    position: absolute; right: 22px; top: 122px; text-align: right;
    color: var(--text-dark);
  }
  .identity__name { font-weight: 700; font-size: 15px; }
  .identity__role { font-weight: 500; font-size: 10px; margin-top: 2px; }
  .contact {
    position: absolute; left: 22px; bottom: 20px;
    list-style: none; display: flex; flex-direction: column; gap: 7px;
    color: var(--text-dark); font-size: 12.5px; font-weight: 500;
  }
  .contact__item { display: flex; align-items: center; gap: 10px; }
  .contact__icon { width: 15px; height: 15px; flex: none; }
</style>
</head>
<body>
<main class="sheet">

  <section class="card card--front" aria-label="Card front">
    <div class="wordmark">
      <div class="wordmark__row">
        <span class="wordmark__dot"></span>
        <span class="wordmark__name">Tobias Wrenfield</span>
      </div>
      <span class="wordmark__role">Cinematographer</span>
    </div>
  </section>

  <section class="card card--back" aria-label="Card back">
    <svg class="card__shape" viewBox="0 0 530 303" preserveAspectRatio="none" aria-hidden="true">
      <defs>
        <linearGradient id="backDark" x1="0" y1="0" x2="1" y2="1">
          <stop offset="0" stop-color="#2a2a2e"/>
          <stop offset="1" stop-color="#111113"/>
        </linearGradient>
        <linearGradient id="backLight" x1="0" y1="0" x2="1" y2="1">
          <stop offset="0" stop-color="#ffffff"/>
          <stop offset="1" stop-color="#e6e6e8"/>
        </linearGradient>
      </defs>
      <rect width="530" height="303" fill="url(#backLight)"/>
      <path d="M0 0 H530 V54 C420 100 230 150 0 178 Z" fill="url(#backDark)"/>
      <path d="M530 54 C420 100 230 150 0 178" fill="none" stroke="#1aa3e0" stroke-width="5"/>
    </svg>

    <div class="wordmark">
      <div class="wordmark__row">
        <span class="wordmark__dot"></span>
        <span class="wordmark__name">Tobias Wrenfield</span>
      </div>
      <span class="wordmark__role">Cinematographer</span>
    </div>

    <div class="identity">
      <p class="identity__name">Tobias Wrenfield</p>
      <p class="identity__role">Cinematographer</p>
    </div>

    <ul class="contact">
      <li class="contact__item">
        <svg class="contact__icon" viewBox="0 0 16 16" aria-hidden="true">
          <rect x="1" y="3" width="14" height="10" rx="1" fill="#1a6fd0"/>
          <path d="M1.5 3.8 L8 9 L14.5 3.8" fill="none" stroke="#fff" stroke-width="1.3"/>
        </svg>
        tkwrenfield@quillbox.example
      </li>
      <li class="contact__item">
        <svg class="contact__icon" viewBox="0 0 16 16" aria-hidden="true">
          <path d="M4 1.5 L6.5 4.5 L5 6.2 C6 8.3 7.7 10 9.8 11 L11.5 9.5 L14.5 12 L13 14.5 C7 14 2 9 1.5 3 Z" fill="#1a6fd0"/>
        </svg>
        503.618.2907
      </li>
      <li class="contact__item">
        <svg class="contact__icon" viewBox="0 0 16 16" aria-hidden="true">
          <circle cx="8" cy="8" r="6.8" fill="#1a6fd0"/>
          <path d="M1.5 8 H14.5 M8 1.2 C5 4.5 5 11.5 8 14.8 M8 1.2 C11 4.5 11 11.5 8 14.8" fill="none" stroke="#fff" stroke-width="1"/>
        </svg>
        www.tobiaswrenfield.example
      </li>
    </ul>
  </section>

</main>
</body>
</html>
```